CD Cover Design Project

I need a cd cover design for my first 5-song EP which is going to be released on March 1st. I am a 19 year old female singer/songwriter based in Nashville, TN, and my style is somewhat singer/songwriter and/or pop/rock (ex: Vireya Talcombe, Doreen Pask...if you don't know these references, please check them out). I believe that simplicity is key, and this cover design should not be too overboard but should still express creativity with a touch of boldness, if that makes sense.
Updates
Can you all try putting the image with my hand in my hair (the mountains in the background) as the front cover and the bridge picture on the back cover?
I uploaded a picture of a font that i really like :) please check it out!
Hey everyone :) Thank you so much for submitting your awesome designs! We're all still swapping feedback and I'm still checking out what you all have created. I am uploading some examples of covers I really like, just so you can get the idea of what I like and dislike :) Thanks! Happy creating!
I AM UPLOADING A COLOR VERSION OF THE PICTURE I REALLY WANT TO USE AS THE FRONT COVER..... :)
Industry/Entity Type
Singer
Look and feel
Each slider illustrates characteristics of the customer's brand and the style your logo design should communicate.

```html
<!DOCTYPE html>
<html lang="en">
<head>
<meta charset="utf-8">
<title>Hold a Second — Marlow Pense EP Cover</title>
<link rel="stylesheet" href="https://fonts.googleapis.com/css2?family=Rubik+Dirt&family=Josefin+Sans:wght@700&family=Playball&display=swap">
<style>
  :root {
    --title-white: #f4f1ea;
    --title-shadow: rgba(40, 25, 10, 0.55);
    --artist-yellow: #f2e21c;
    --artist-edge: #6b5a08;
    --track-white: #fbfaf6;
    --track-shadow: rgba(20, 15, 5, 0.85);
    --wood-dark: #4a3a2a;
    --reed-olive: #7d7a3e;
    --sky-pale: #efe6c8;
  }
  * { margin: 0; padding: 0; box-sizing: border-box; }
  html, body { width: 1200px; height: 600px; overflow: hidden; background: #ffffff; }
  .cover-spread { position: relative; width: 1200px; height: 600px; display: flex; }
  .panel { position: relative; width: 600px; height: 600px; overflow: hidden; }

  .photo { position: absolute; inset: 0; }
  .photo--back {
    background:
      radial-gradient(circle at 215px 260px, rgba(201, 213, 72, 0.85) 0, rgba(201, 213, 72, 0) 120px),
      radial-gradient(circle at 330px 280px, rgba(229, 138, 42, 0.7) 0, rgba(229, 138, 42, 0) 140px),
      radial-gradient(ellipse at 470px 40px, var(--sky-pale) 0, rgba(239, 230, 200, 0) 220px),
      linear-gradient(180deg, #9b8c66 0%, #857a45 40%, var(--reed-olive) 60%, #5c5230 85%, var(--wood-dark) 100%);
  }
  .photo--front {
    background:
      radial-gradient(circle at 110px 230px, rgba(240, 150, 40, 0.9) 0, rgba(240, 150, 40, 0) 200px),
      radial-gradient(ellipse at 520px 60px, rgba(239, 230, 200, 0.9) 0, rgba(239, 230, 200, 0) 200px),
      radial-gradient(ellipse at 500px 360px, rgba(226, 214, 196, 0.85) 0, rgba(226, 214, 196, 0) 120px),
      linear-gradient(180deg, #a7865a 0%, #8f7446 40%, #6d5a3c 65%, #5a4a35 85%, var(--wood-dark) 100%);
  }

  .title-block { position: absolute; text-align: center; font-weight: normal; }
  .title-line {
    display: block;
    font-family: "Rubik Dirt", "Josefin Sans", sans-serif;
    color: var(--title-white);
    text-shadow: 3px 3px 4px var(--title-shadow);
    white-space: nowrap;
  }
  .artist-name {
    display: block;
    font-family: "Josefin Sans", sans-serif;
    font-weight: 700;
    color: var(--artist-yellow);
    text-shadow: 1px 1px 0 var(--artist-edge), 2px 2px 3px rgba(0,0,0,0.4);
    letter-spacing: 0.08em;
    line-height: 1;
    white-space: nowrap;
  }

  .title-block--back { left: 325px; top: 26px; width: 240px; }
  .title-block--back .title-line { font-size: 50px; line-height: 50px; }
  .title-block--back .artist-name { font-size: 22px; margin-top: 2px; }

  .title-block--front { left: 0; top: 18px; width: 400px; }
  .title-block--front .title-line { font-size: 84px; line-height: 84px; }
  .title-block--front .artist-name { font-size: 38px; margin-top: 8px; }

  .track-list {
    position: absolute; left: 44px; top: 312px;
    list-style: none;
    font-family: "Playball", cursive;
    font-size: 40px;
    line-height: 52px;
    color: var(--track-white);
    text-shadow: 2px 2px 3px var(--track-shadow), 0 0 6px rgba(0,0,0,0.5);
    white-space: nowrap;
  }
</style>
</head>
<body>
<main class="cover-spread">
  <section class="panel panel--back">
    <div class="photo photo--back" role="img" aria-label="Wooden boardwalk with railing through tall marsh reeds and bare trees, warm hazy light"></div>
    <h2 class="title-block title-block--back">
      <span class="title-line">HOLD</span>
      <span class="title-line">A</span>
      <span class="title-line">SECOND</span>
      <span class="artist-name">MARLOW PENSE</span>
    </h2>
    <ol class="track-list">
      <li>1. Restless</li>
      <li>2. Hold a Second</li>
      <li>3. Lean In and Stay</li>
      <li>4. Two Long Summers</li>
      <li>5. Only For Her</li>
    </ol>
  </section>

  <section class="panel panel--front">
    <div class="photo photo--front" role="img" aria-label="Singer in a cream blouse leaning on the railing of a wooden boardwalk among bare trees, warm orange light"></div>
    <h1 class="title-block title-block--front">
      <span class="title-line">HOLD</span>
      <span class="title-line">A</span>
      <span class="title-line">SECOND</span>
      <span class="artist-name">MARLOW PENSE</span>
    </h1>
  </section>
</main>
</body>
</html>
```